create a webpage for optometry practice

I'm looking to create a professional and elegant webpage for my practice. I prefer neutral earthy colors, but I am open to other ideas. I have included an image of my logo to be used in the process. This will be a page that will illustrate information about my practice and the kind of services we offer. I am in process of having the practice remodeled. So I don't have any photos of my practice to include yet.

Target Market(s)

My practice serves young and mature families.

Industry/Entity Type

It Professional

Number of Pages Required

5+ page

Font styles to use
Sans Serif

Colors
33a6d7
86cfc6
85cae6
cadf82
3276b5
faa54b
abd036
f78c1e

Requirements
Must have
• I would need to incorporate information about my practice, services, insurance accepted, make appointment, contact us, and about our family.
Nice to have
• I would like to see something fresh, modern, and unique

```html
<!DOCTYPE html>
<html lang="en">
<head>
<meta charset="utf-8">
<title>Lumera Eye Care</title>
<link href="https://fonts.googleapis.com/css2?family=Mulish:wght@300;400;500;600&display=swap" rel="stylesheet">
<style>
  :root {
    --blue: #33a6d7;
    --blue-soft: #85cae6;
    --blue-deep: #3276b5;
    --green: #abd036;
    --green-light: #cadf82;
    --orange: #f78c1e;
    --orange-light: #faa54b;
    --ink: #2b2b2b;
    --grey-text: #555;
    --field-border: #d5d5d5;
    --white: #fff;
  }
  * { box-sizing: border-box; margin: 0; padding: 0; }
  html, body { width: 944px; height: 1200px; overflow: hidden; }
  body {
    position: relative;
    font-family: "Mulish", Arial, sans-serif;
    color: var(--ink);
    background: var(--white);
  }
  .page-top-band {
    position: absolute; left: 0; top: 126px; width: 944px; height: 300px;
    background: linear-gradient(#ededed, #fff);
  }
  /* header */
  .brand {
    position: absolute; left: 150px; top: 38px;
    display: flex; align-items: center; gap: 10px;
  }
  .brand-dot { width: 26px; height: 26px; border-radius: 50%; background: var(--blue); }
  .brand-name { font-size: 23px; font-weight: 400; color: #4a4a4a; letter-spacing: 0.5px; white-space: nowrap; }
  .enquiry { position: absolute; right: 164px; top: 48px; text-align: right; }
  .enquiry-label { font-size: 12px; color: var(--blue); }
  .enquiry-phone { font-size: 18px; color: #555; margin-top: 1px; }
  /* nav */
  .main-nav {
    position: absolute; left: 150px; top: 92px; width: 644px; height: 35px;
    background: linear-gradient(#a8d23a, #8ec21e);
    display: flex;
  }
  .main-nav a {
    flex: none; white-space: nowrap; text-align: center;
    color: var(--white); text-decoration: none; font-size: 12px;
    line-height: 35px;
    border-right: 1px solid rgba(255,255,255,0.25);
  }
  .main-nav a:last-child { border-right: none; }
  .nav-home { width: 75px; }
  .nav-about { width: 106px; }
  .nav-services { width: 75px; }
  .nav-insurance { width: 80px; }
  .nav-appointment { width: 103px; }
  .nav-family { width: 87px; }
  .nav-contact { width: 118px; text-align: left !important; padding-left: 14px; }
  /* hero */
  .hero {
    position: absolute; left: 148px; top: 127px; width: 646px; height: 278px;
    overflow: hidden; border-radius: 0 0 3px 3px;
  }
  .hero-photo {
    position: absolute; inset: 0;
    background: linear-gradient(100deg, #dfe4e8 0%, #c9cfd4 40%, #9aa6b2 70%, #4c5258 100%);
  }
  .hero-overlay { position: absolute; left: 0; top: 0; }
  .hero-copy { position: absolute; left: 26px; top: 88px; color: var(--white); }
  .hero-title { font-size: 23px; font-weight: 400; white-space: nowrap; }
  .hero-sub { font-size: 14.5px; font-weight: 300; margin-top: 3px; white-space: nowrap; }
  .hero-text { font-size: 7.8px; line-height: 13.5px; margin-top: 7px; width: 220px; }
  .hero-dots { display: flex; gap: 3px; margin-top: 10px; }
  .hero-dots span { width: 11px; height: 11px; border-radius: 50%; background: var(--white); }
  .hero-dots span.active { background: #111; }
  /* about */
  .about { position: absolute; left: 0; top: 444px; width: 944px; text-align: center; }
  .about h1 { font-size: 24px; font-weight: 400; color: #222; }
  .about-lead { font-size: 12px; margin-top: 11px; color: #333; }
  .about-text { font-size: 7.4px; line-height: 13.3px; color: #555; width: 590px; margin: 7px auto 0; }
  /* tiles */
  .tile { position: absolute; top: 585px; width: 207px; height: 128px; overflow: hidden; }
  .tile-photo { height: 93px; }
  .tile-label {
    height: 35px; line-height: 37px; text-align: center;
    color: var(--white); font-size: 14.5px; white-space: nowrap;
  }
  .tile-services { left: 151px; }
  .tile-services .tile-photo { background: linear-gradient(90deg, #e8d2b0, #e9edf1 50%, #d7c3c8); }
  .tile-services .tile-label { background: var(--blue); }
  .tile-insurance { left: 369px; }
  .tile-insurance .tile-photo { background: linear-gradient(#4d8fcf, #7fb3df 60%, #5d89b8); }
  .tile-insurance .tile-label { background: var(--orange-light); }
  .tile-family { left: 587px; }
  .tile-family .tile-photo { background: linear-gradient(90deg, #2f2f2f, #c99a7a 45%, #e6e8ea); }
  .tile-family .tile-label { background: #9cc93a; }
  /* appointment */
  .appointment {
    position: absolute; left: 0; top: 757px; width: 944px; height: 220px;
    border-top: 1px solid #dcdcdc;
    background: linear-gradient(#fff, #ececec);
  }
  .appointment h2 {
    position: absolute; left: 0; top: 42px; width: 944px; text-align: center;
    font-size: 20px; font-weight: 400; color: #333;
  }
  .field {
    position: absolute; width: 167px; height: 25px;
    border: 1px solid var(--field-border); background: #f6f6f6;
    font-size: 8.5px; color: #555; line-height: 23px; padding-left: 10px;
  }
  .field svg { position: absolute; right: 10px; top: 8px; }
  .book-btn {
    position: absolute; left: 406px; top: 157px; width: 131px; height: 31px;
    background: linear-gradient(#a8d23a, #8ec21e);
    color: var(--white); font-size: 11px; text-align: center; line-height: 31px;
  }
  /* footer */
  .site-footer {
    position: absolute; left: 0; top: 977px; width: 944px; height: 171px;
    background: linear-gradient(#55b7df, #2f9ad3);
    color: var(--white);
  }
  .footer-col { position: absolute; top: 32px; }
  .footer-col h3 { font-size: 15px; font-weight: 300; color: rgba(255,255,255,0.75); margin-bottom: 9px; white-space: nowrap; }
  .footer-col li { list-style: none; font-size: 9px; line-height: 18.5px; white-space: nowrap; }
  .social { display: flex; gap: 8px; margin-top: 7px; }
  .social span { width: 14px; height: 14px; border-radius: 50%; background: var(--white); }
  .footer-bar {
    position: absolute; left: 0; top: 1148px; width: 944px; height: 52px;
    background: #3a9fd6; font-size: 7px; color: rgba(255,255,255,0.7);
    padding: 20px 0 0 152px;
  }
</style>
</head>
<body>
  <div class="page-top-band"></div>

  <header>
    <div class="brand"><span class="brand-dot"></span><span class="brand-name">Lumera Eye Care</span></div>
    <div class="enquiry">
      <div class="enquiry-label">Enquiry Now</div>
      <div class="enquiry-phone">555.014.2290</div>
    </div>
  </header>

  <nav class="main-nav">
    <a class="nav-home" href="#">Home</a><a class="nav-about" href="#">About Practise</a><a class="nav-services" href="#">Services</a><a class="nav-insurance" href="#">Insurance</a><a class="nav-appointment" href="#">Appointment</a><a class="nav-family" href="#">Our Family</a><a class="nav-contact" href="#">Contact us</a>
  </nav>

  <section class="hero">
    <div class="hero-photo" role="img" aria-label="Optometrist examining a senior patient's eyes beside a phoropter"></div>
    <svg class="hero-overlay" width="646" height="278" viewBox="0 0 646 278">
      <polygon points="0,0 226,0 302,278 0,278" fill="#3fa8dc" fill-opacity="0.88"/>
      <polygon points="0,0 150,0 60,278 0,278" fill="#6fbde4" fill-opacity="0.35"/>
      <polygon points="80,278 302,278 240,120" fill="#2f8fcc" fill-opacity="0.35"/>
    </svg>
    <div class="hero-copy">
      <div class="hero-title">Optometry Practise</div>
      <div class="hero-sub">Cras a ante vitae enim</div>
      <p class="hero-text">Pellentesque faucibus Ut accumsan ultricies elit Maecenas at justo id velit placerat molestie Donec</p>
      <div class="hero-dots"><span class="active"></span><span></span><span></span><span></span></div>
    </div>
  </section>

  <section class="about">
    <h1>About Lumera Eye Care</h1>
    <p class="about-lead">Class aptent taciti sociosqu ad litora torquent per conubia nostra per inceptos hymenaeos Proin nulla</p>
    <p class="about-text">Mauris vel lacus vitae felis vestibulum volutpat Etiam est nunc venenatis in tristique eu imperdiet ac nisl Cum sociis natoque penatibus et magnis dis parturient montes nascetur ridiculus mus In iaculis facilisis massa Etiam eu urna Sed porta Suspendisse quam leo molestie sed luctus quis feugiat in pede Fusce tellus Sed metus augue convallis et vehicula ut pulvinar eu ante Integer orci tellus tristique vitae consequat necCras a ante vitae enim iaculis aliquam Mauris nunc quam</p>
  </section>

  <a class="tile tile-services"><div class="tile-photo" role="img" aria-label="Young woman at a slit lamp eye examination"></div><div class="tile-label">Our Services</div></a>
  <a class="tile tile-insurance"><div class="tile-photo" role="img" aria-label="Businessman in glasses against a blue sky"></div><div class="tile-label">Insurance</div></a>
  <a class="tile tile-family"><div class="tile-photo" role="img" aria-label="Patient having an eye test in a clinic"></div><div class="tile-label">Our Family</div></a>

  <section class="appointment">
    <h2>Make an Appointment with Our Eye Specialist</h2>
    <div class="field" style="left:222px;top:85px">Your Name</div>
    <div class="field" style="left:396px;top:85px">Email address</div>
    <div class="field" style="left:570px;top:85px">Phone no.</div>
    <div class="field" style="left:222px;top:117px">Date Preffered<svg width="9" height="6" viewBox="0 0 9 6"><path d="M1 1l3.5 3.5L8 1" fill="none" stroke="#444" stroke-width="1.3"/></svg></div>
    <div class="field" style="left:396px;top:117px">Time Preffered<svg width="9" height="6" viewBox="0 0 9 6"><path d="M1 1l3.5 3.5L8 1" fill="none" stroke="#444" stroke-width="1.3"/></svg></div>
    <div class="field" style="left:570px;top:117px">City/Location</div>
    <div class="book-btn">Book Appointment</div>
  </section>

  <footer class="site-footer">
    <div class="footer-col" style="left:153px">
      <h3>Quick Links</h3>
      <ul><li>What We Do</li><li>About Practice</li><li>Make an Appointment</li><li>Insurance</li></ul>
    </div>
    <div class="footer-col" style="left:301px">
      <h3>Services</h3>
      <ul><li>Cras a ante vitae enim</li><li>Eaculis aliquam Mauris</li><li>Nquam venenatis</li><li>Euismod sit</li></ul>
    </div>
    <div class="footer-col" style="left:458px">
      <h3>Resources</h3>
      <ul><li>Our family</li><li>Contact us</li><li>Term of Use</li></ul>
    </div>
    <div class="footer-col" style="left:597px">
      <h3>Follow Us</h3>
      <ul><li>Please connect with us on these</li></ul>
      <div class="social"><span></span><span></span><span></span><span></span></div>
    </div>
  </footer>
  <div class="footer-bar">© 2015 Company Name &nbsp;All right reserved &nbsp;Term of Use</div>
</body>
</html>
```